Would like a website to blog, vlog and post pictures about a upcoming glowtrek road trip in a 1977 kx van.
We will have custom bumper stickers available (by donation or a set amount - unsure) and would like to be able mail these out in the future.
Would like the website to be easy to use, simple. clean with a modern hippie/boho feel.
The travelling van is original green. We have a custom lic plate 'glowtrek'
The stickers are black, white and red.
Our mission:
A Love movement journey to raise the vibration and awareness of Boundless Glow.
We plan to have it painted with washable paint at certain spots along the way. We will ask willing people to make a journal entry of how they glowtrek (spread the love) and I will quote them in my blog or blog.
The picture attached is me, Dorinda after we painted "Breezy" (the van's given name) with friends for a Canada Day celebration.
The road trip is with my boyfriend and our two 13yr olds - a boy and a girl.
However, the road trip in August is just the beginning of what I envision to be a much longer journey...so I would like the website created to hold space for future adventures :)
Happy creating to whomever feels their heart strings pulled to be part of our glowtrek journey!
With Love and Gratitude,
Dorinda (Band of Sunrise:)
Please note:
KX pic is for inspiration only - please do not use it on the site. Thank you.

Industry/Entity Type

Paint

Requirements
Must have
• Opt in for Future Newsletter, blog, vlog, join the movement - permission to get creative ;)
Email: dorinda@glowtrek.example

```html
<!DOCTYPE html>
<html lang="en">
<head>
<meta charset="utf-8">
<title>glowtrek — join the movement</title>
<link href="https://fonts.googleapis.com/css2?family=Roboto+Condensed:wght@300;400;700&family=Arimo:wght@400;700&display=swap" rel="stylesheet">
<style>
:root{
  --bg:#000;
  --panel:#1d1d1d;
  --panel-2:#2a2a2a;
  --footer:#121212;
  --red:#d40000;
  --white:#fff;
  --text:#cfcfcf;
  --muted:#7d7d7d;
  --line:#3a3a3a;
}
*{margin:0;padding:0;box-sizing:border-box}
html,body{width:1030px;height:1200px;overflow:hidden;background:var(--bg)}
body{position:relative;font-family:"Arimo",Arial,sans-serif;color:var(--text);font-size:8px}
.abs{position:absolute}
.heading{font-family:"Roboto Condensed",Arial,sans-serif;font-weight:300;font-size:16px;color:#e6e6e6;letter-spacing:-.2px}
.heading em{font-style:normal;color:var(--red)}
.photo{position:absolute}

/* header */
.brand{left:0;width:1030px;top:22px;text-align:center}
.brand-name{font-family:"Roboto Condensed",Arial,sans-serif;font-weight:700;font-size:40px;line-height:40px;color:var(--white);letter-spacing:1px;display:inline-flex;align-items:center;gap:6px}
.brand-name .dot{width:22px;height:22px;border-radius:50%;background:var(--red);display:inline-block}
.brand-url{font-family:"Roboto Condensed",Arial,sans-serif;font-weight:700;font-size:10px;color:var(--white);letter-spacing:1px;margin-left:-20px}
.search{left:672px;top:74px;width:88px;height:20px;border:1px solid #555;color:#666;font-size:7px;padding:5px 0 0 22px}
.search svg{position:absolute;left:6px;top:5px}
.rule{left:257px;width:503px;height:1px;background:var(--line)}
.nav{left:257px;top:111px;font-size:8px;color:#aaa}
.nav span{margin:0 4px;color:#666}
.movement{left:672px;top:107px;font-size:9px;color:#ddd;display:flex;align-items:center;gap:4px}

/* blogs */
.feature-cap{left:257px;top:277px;width:281px;height:51px;background:rgba(60,60,60,.85);padding:12px 10px}
.feature-cap h3{font-weight:400;font-size:9px;color:#eee;margin-bottom:4px}
.feature-cap p{font-size:6.5px;color:#ddd;white-space:nowrap}
.tile-cap{font-size:8px;color:#bbb}
.tile-text{font-size:6px;color:#ccc;line-height:1.35}

/* cards */
.card{position:absolute;left:257px;width:203px;height:190px;background:var(--panel);padding:19px 15px 0}
.card h4{font-weight:400;font-size:9px;line-height:12px;color:#e8e8e8}
.card .date{font-size:6.5px;line-height:8px;color:var(--muted);margin-top:4px}
.card .pic{width:173px;height:70px;margin-top:9px}
.card p{font-size:5.6px;line-height:9px;color:#888;margin-top:13px;white-space:nowrap}
.card .foot{position:absolute;left:15px;right:15px;bottom:11px;height:12px;display:flex;justify-content:space-between;align-items:center}
.card .icons{display:flex;gap:4px}
.card .icons i{width:12px;height:12px;border-radius:50%;border:1px solid #555;display:block}
.card .more{font-size:6.5px;color:var(--muted)}
.card.active{background:var(--red)}
.card.active h4,.card.active .date,.card.active p,.card.active .more{color:var(--white)}
.card.active .icons i{background:var(--white);border-color:var(--white)}

/* video */
.video{left:467px;top:395px;width:293px;height:251px;background:var(--panel)}
.tabs{position:absolute;left:10px;top:12px;display:flex;gap:3px}
.tabs b{width:17px;height:13px;background:#555;color:#ddd;font-weight:400;font-size:7px;text-align:center;line-height:13px}
.tabs b.on{background:var(--red)}
.player{position:absolute;left:9px;top:33px;width:274px;height:156px;background:#0b0b0b}
.controls{position:absolute;left:6px;top:130px;width:262px;height:20px;display:flex;align-items:center;gap:6px}
.play{width:26px;height:18px;background:#1a1a1a;display:flex;align-items:center;justify-content:center}
.track{flex:1;height:6px;border:1px solid #2f6b6b;background:#173535}
.hd{font-size:8px;font-weight:700;color:#36a9c9;font-style:italic}
.video p{position:absolute;left:10px;top:208px;width:270px;font-size:6.5px;line-height:1.6;color:#aaa}
.video .more{position:absolute;left:10px;top:231px;font-size:6.5px;color:var(--muted)}

/* news */
.news{left:467px;top:706px;width:175px}
.news-item{margin-bottom:19px}
.news-item h5{font-size:7px;font-weight:700;color:#eee;line-height:1.5}
.news-item h5 small{font-weight:400;font-style:italic;font-size:6px;color:var(--muted)}
.news-item p{font-size:6.5px;line-height:1.5;color:#888;margin-top:3px}
.social{position:absolute;left:654px;width:106px;height:79px;background:var(--panel);text-align:center;padding-top:26px}
.social .ring{width:14px;height:14px;border-radius:50%;background:#8a8a8a;margin:0 auto 8px}
.social span{font-size:9px;color:#ddd}

/* footer */
.footer{left:0;top:1008px;width:1030px;height:192px;background:var(--footer)}
.f-brand{left:257px;top:1036px;font-family:"Roboto Condensed",Arial,sans-serif;font-weight:700;font-size:24px;color:var(--white);display:flex;align-items:center;gap:4px}
.f-brand .dot{width:13px;height:13px;border-radius:50%;background:var(--red)}
.f-url{left:282px;top:1062px;font-family:"Roboto Condensed",Arial,sans-serif;font-weight:700;font-size:7px;color:var(--white);letter-spacing:1px}
.archive{left:427px;top:1068px;list-style:none}
.archive li{font-size:6.5px;color:#bbb;height:12px}
.archive li::before{content:"\00BB";color:#666;margin-right:8px}
.archive li.on{color:var(--red);text-decoration:underline}
.signup{left:554px;top:1068px;width:172px;height:24px;background:#000;display:flex;align-items:center}
.signup .field{flex:1;font-size:6.5px;color:#666;padding-left:9px;display:flex;align-items:center;gap:8px}
.signup .go{width:24px;height:24px;background:var(--red);display:flex;align-items:center;justify-content:center}
.copyright{left:257px;top:1182px;font-size:6px;color:#777}
.legal{left:628px;top:1182px;width:132px;text-align:right;font-size:6px;color:#999}
.legal span{color:#666;margin:0 3px}
.legal .on{color:var(--red);text-decoration:underline}
</style>
</head>
<body>

<header>
  <div class="abs brand">
    <div class="brand-name">glowtrek<i class="dot"></i></div><br>
    <span class="brand-url">glowtrek.ca</span>
  </div>
  <div class="abs search">
    <svg width="9" height="9" viewBox="0 0 9 9"><circle cx="3.6" cy="3.6" r="2.8" fill="none" stroke="#777" stroke-width="1"/><line x1="5.7" y1="5.7" x2="8.5" y2="8.5" stroke="#777" stroke-width="1.2"/></svg>
    search blog
  </div>
  <div class="abs rule" style="top:102px"></div>
  <nav class="abs nav">Our Recent Blogs<span>|</span>About Us<span>|</span>Custom Link</nav>
  <div class="abs movement">
    <svg width="10" height="9" viewBox="0 0 10 9"><path d="M5 9 L0.8 4.6 A2.4 2.4 0 0 1 5 1.6 A2.4 2.4 0 0 1 9.2 4.6 Z" fill="#d40000"/></svg>
    join the movement
  </div>
</header>

<main>
  <h2 class="abs heading" style="left:257px;top:156px">recent <em>blogs</em></h2>
  <h2 class="abs heading" style="left:544px;top:156px">images</h2>

  <div class="photo" role="img" aria-label="Close-up of rows of round LED bulbs" style="left:257px;top:184px;width:281px;height:144px;background:linear-gradient(135deg,#e9e9e4,#bdbdb6 55%,#e6da6a)"></div>
  <div class="abs feature-cap">
    <h3>HEADING OF TITLE</h3>
    <p>Lorem Ipsum is simply dummy text of the printing and typesetting industry. Lorem Ipsum has been</p>
  </div>

  <div class="photo" role="img" aria-label="Portrait photo against a blue sky" style="left:544px;top:184px;width:105px;height:60px;background:linear-gradient(160deg,#7fb4d6,#3f7aa6)"></div>
  <div class="photo" role="img" aria-label="Photo of a figure by a bright window" style="left:544px;top:247px;width:105px;height:81px;background:linear-gradient(160deg,#9bb1bd,#4a5a66)"></div>
  <div class="abs tile-cap" style="left:553px;top:314px">HEADING</div>
  <div class="photo" role="img" aria-label="Warm sepia portrait photo" style="left:654px;top:184px;width:104px;height:79px;background:linear-gradient(160deg,#6d5440,#3a2c22)"></div>
  <div class="abs tile-cap" style="left:663px;top:192px;color:#eee">HEADING</div>
  <div class="abs tile-text" style="left:663px;top:209px;width:86px">Lorem Ipsum is simply dummy text of the printing and typeset ting industry. Lorem Ipsum has been</div>
  <div class="photo" role="img" aria-label="Portrait photo in warm evening light" style="left:654px;top:268px;width:104px;height:60px;background:linear-gradient(160deg,#4b3a34,#a0705a)"></div>

  <h2 class="abs heading" style="left:257px;top:367px">welcome you!</h2>
  <h2 class="abs heading" style="left:467px;top:367px">video slideshow <em>update</em></h2>

  <article class="card" style="top:395px">
    <h4>This is a demo heading</h4>
    <div class="date">Upload Date 22 July 2014</div>
    <div class="pic" role="img" aria-label="Black and white clock face beside a world map" style="background:linear-gradient(90deg,#e8e8e8,#8a8a8a 55%,#dcdcdc)"></div>
    <p>Lorem Ipsum is simply dummy text of the printing and typeset-<br>ting industry. Lorem Ipsum has been the industry's standard</p>
    <div class="foot"><div class="icons"><i></i><i></i></div><span class="more">+ read more</span></div>
  </article>

  <article class="card active" style="top:590px">
    <h4>This is a demo heading</h4>
    <div class="date">Upload Date 22 July 2014</div>
    <div class="pic" role="img" aria-label="Photo of a girl hugging her dog outdoors" style="background:linear-gradient(90deg,#6f7d3c,#3a2a22 50%,#a06a40)"></div>
    <p>Lorem Ipsum is simply dummy text of the printing and typeset-<br>ting industry. Lorem Ipsum has been the industry's standard</p>
    <div class="foot"><div class="icons"><i></i><i></i></div><span class="more">+ read more</span></div>
  </article>

  <article class="card" style="top:787px">
    <h4>This is a demo heading</h4>
    <div class="date">Upload Date 22 July 2014</div>
    <div class="pic" role="img" aria-label="Silhouette by a lake at sunset" style="background:linear-gradient(180deg,#8a8f95,#d9c9a0 40%,#3a3a3a 55%,#8b8a85)"></div>
    <p>Lorem Ipsum is simply dummy text of the printing and typeset-<br>ting industry. Lorem Ipsum has been the industry's standard</p>
    <div class="foot"><div class="icons"><i></i><i></i></div><span class="more">+ read more</span></div>
  </article>

  <section class="abs video">
    <div class="tabs"><b class="on">1</b><b>2</b><b>3</b><b>4</b></div>
    <div class="player">
      <div class="photo" role="img" aria-label="Video still of a woman with raised arms by the sea" style="left:6px;top:6px;width:262px;height:120px;background:linear-gradient(180deg,#5d9ac8,#8cc0df 60%,#e2e6ea)"></div>
      <div class="controls">
        <div class="play"><svg width="8" height="9" viewBox="0 0 8 9"><path d="M0 0 L8 4.5 L0 9 Z" fill="#ddd"/></svg></div>
        <div class="track"></div>
        <span class="hd">HD</span>
        <svg width="10" height="10" viewBox="0 0 10 10" fill="none" stroke="#bbb" stroke-width="1.2"><path d="M1 4V1H4M6 1H9V4M9 6V9H6M4 9H1V6"/></svg>
      </div>
    </div>
    <p>Lorem Ipsum is simply dummy text of the printing and typesetting industry. Lorem Ipsum has been the industry's standard</p>
    <span class="more">+ view more</span>
  </section>

  <h2 class="abs heading" style="left:467px;top:673px">latest <em>news</em></h2>
  <h2 class="abs heading" style="left:654px;top:673px">connect</h2>

  <section class="abs news">
    <div class="news-item">
      <h5>Lorem Ipsum is simply dummy text of the printing <small>- 22 July 2014 by Admin</small></h5>
      <p>Lorem Ipsum is simply dummy text of the printing and type-setting has been the industry's standard</p>
    </div>
    <div class="news-item">
      <h5>Lorem Ipsum is simply<br>dummy <small>- 22 July 2014 by Admin</small></h5>
      <p>Lorem Ipsum is simply dummy text of the printing and type-setting</p>
    </div>
    <div class="news-item">
      <h5>Lorem dummy text of the<br>printing <small>- 22 July 2014 by Admin</small></h5>
      <p>Lorem Ipsum is simply typesetting has been the industry's standard</p>
    </div>
    <div class="news-item">
      <h5>Lorem dummy text of the<br>printing <small>- 22 July 2014 by Admin</small></h5>
      <p>Lorem Ipsum is simply typesetting has been the industry's standard</p>
    </div>
  </section>

  <a class="social" style="top:707px"><div class="ring"></div><span>friendbook</span></a>
  <a class="social" style="top:793px"><div class="ring"></div><span>chirper</span></a>
</main>

<footer>
  <div class="abs footer"></div>
  <div class="abs f-brand">glowtrek<i class="dot"></i></div>
  <div class="abs f-url">glowtrek.ca</div>
  <h2 class="abs heading" style="left:427px;top:1036px">archive</h2>
  <ul class="abs archive">
    <li>JULY</li><li>AUGUST</li><li class="on">SEPTEMBER</li><li>OCTOBER</li><li>NOVEMBER</li><li>DECEMBER</li>
  </ul>
  <h2 class="abs heading" style="left:554px;top:1036px">signup <em>newsletter</em></h2>
  <div class="abs signup">
    <div class="field">
      <svg width="9" height="6" viewBox="0 0 9 6"><rect x="0.5" y="0.5" width="8" height="5" fill="none" stroke="#666"/><path d="M0.5 0.5 L4.5 3.5 L8.5 0.5" fill="none" stroke="#666"/></svg>
      Enter Your Email
    </div>
    <div class="go"><svg width="10" height="8" viewBox="0 0 10 8"><path d="M1 4 L4 7 L9 1" fill="none" stroke="#fff" stroke-width="1.6"/></svg></div>
  </div>
  <div class="abs rule" style="top:1166px"></div>
  <div class="abs copyright">Copyright All Right Reserved</div>
  <div class="abs legal">Videos<span>|</span><span class="on" style="margin:0">Blog</span><span>|</span>Privacy Policy<span>|</span>Terms of Uses</div>
</footer>

</body>
</html>
```